KALVENTO Amazing Business Cards Challenge

Kalvent is a new technology company that will provide engineering and manufacturing services in the electric vehicle industry.

We are looking at a new business card that will support our orientation in providing advanced, innovative solutions. The business card will be lean and present the only information required to be more efficient.

Target Market(s)

Fleet operators, private commercial vehicle operators, delivery companies.

Industry/Entity Type

Business

Contact Information for Business Card

Use the logo and its colors, use a white background.

Font styles to use
Sans Serif

Colors
0455a3
ffffff
9bcb3c

Requirements
Must have
• Kalvento Logo
• All informations in the DOC file = 3 different cards.
• White background
Nice to have
• Icons for email, phone and web address.
• Cute design and strong identity.
Should not have
• Bleeds

```html
<!DOCTYPE html>
<html lang="en">
<head>
<meta charset="utf-8">
<title>Kalvento Business Cards</title>
<link href="https://fonts.googleapis.com/css2?family=Open+Sans:wght@400;600;700&display=swap" rel="stylesheet">
<style>
  :root {
    --backdrop: #d9dadc;
    --card: #ffffff;
    --card-edge: #e2e4e6;
    --blue: #0455a3;
    --blue-light: #1a8fd6;
    --green: #9bcb3c;
    --ink: #1d1f22;
    --grey: #6c6e70;
  }
  * { margin: 0; padding: 0; box-sizing: border-box; }
  html, body {
    width: 1200px; height: 844px; overflow: hidden;
    background: var(--backdrop);
    font-family: "Open Sans", Arial, sans-serif;
  }
  .canvas {
    width: 1200px; height: 844px;
    display: grid;
    grid-template-columns: 520px 520px;
    grid-template-rows: 298px 298px;
    gap: 40px;
    justify-content: center;
    align-content: center;
  }
  .card {
    position: relative;
    width: 520px; height: 298px;
    background: var(--card);
    border: 1px solid var(--card-edge);
    border-radius: 3px;
    box-shadow: 0 10px 24px rgba(0,0,0,.18);
    overflow: hidden;
  }
  .card--back { display: flex; align-items: center; justify-content: center; gap: 16px; }

  .brand-name {
    position: absolute; top: 54px; left: 0; width: 100%;
    text-align: center; color: var(--blue);
    font-weight: 700; font-size: 28px; letter-spacing: 1px;
  }
  .holder { position: absolute; left: 28px; bottom: 24px; color: var(--ink); }
  .holder__name { font-weight: 700; font-size: 19px; line-height: 1.3; }
  .holder__name small { font-weight: 400; font-size: 13px; }
  .holder__role { color: var(--blue-light); font-size: 14px; margin-top: 1px; }
  .holder__address { font-size: 13.5px; line-height: 1.4; margin-top: 14px; }

  .contacts {
    position: absolute; right: 24px; top: 128px;
    list-style: none; color: var(--ink); font-size: 13.5px; text-align: right;
  }
  .contacts li { display: flex; align-items: center; justify-content: flex-end; gap: 8px; height: 20px; }
  .icon {
    width: 14px; height: 14px; background: var(--blue-light); border-radius: 2px;
    display: inline-flex; align-items: center; justify-content: center;
  }
  .accent-line {
    position: absolute; left: 0; bottom: 0; width: 100%; height: 5px; background: var(--green);
  }

  .back-mark { width: 40px; height: 40px; background: var(--blue); border-radius: 4px; }
  .back-name { color: var(--grey); font-size: 54px; font-weight: 600; letter-spacing: 2px; }
</style>
</head>
<body>
<main class="canvas">
  <svg width="0" height="0" style="position:absolute" aria-hidden="true">
    <symbol id="i-phone" viewBox="0 0 10 10"><path d="M2 1l2 2-1 1.2c.6 1.2 1.6 2.2 2.8 2.8L7 6l2 2-1.2 1.2C4.5 9 1 5.5.8 2.2z" fill="#fff"/></symbol>
    <symbol id="i-mail" viewBox="0 0 10 10"><rect x="1" y="2.5" width="8" height="5.5" fill="none" stroke="#fff" stroke-width="1"/><path d="M1 2.5l4 3 4-3" fill="none" stroke="#fff" stroke-width="1"/></symbol>
    <symbol id="i-web" viewBox="0 0 10 10"><path d="M4 6l2-2M3.5 4.5L2.3 5.7a1.5 1.5 0 002 2L5.5 6.5M6.5 5.5l1.2-1.2a1.5 1.5 0 00-2-2L4.5 3.5" fill="none" stroke="#fff" stroke-width="1.1" stroke-linecap="round"/></symbol>
  </svg>

  <section class="card card--back">
    <span class="back-mark"></span>
    <span class="back-name">kalvento</span>
    <span class="accent-line"></span>
  </section>

  <section class="card card--front">
    <div class="brand-name">kalvento</div>
    <ul class="contacts">
      <li>+1.555.210.0387 <span class="icon"><svg width="10" height="10"><use href="#i-phone"/></svg></span></li>
      <li>mlavallee@kalvento.com <span class="icon"><svg width="10" height="10"><use href="#i-mail"/></svg></span></li>
      <li>kalvento.com <span class="icon"><svg width="10" height="10"><use href="#i-web"/></svg></span></li>
    </ul>
    <div class="holder">
      <p class="holder__name">Mathieu Lavallée <small>P.Eng., MASc</small></p>
      <p class="holder__role">President | CEO</p>
      <p class="holder__address">410-218 Belanger East,<br>Laval (Quebec) Canada H7A 2K9</p>
    </div>
    <span class="accent-line"></span>
  </section>

  <section class="card card--front">
    <div class="brand-name">kalvento</div>
    <ul class="contacts">
      <li>+1.555.210.0412 <span class="icon"><svg width="10" height="10"><use href="#i-phone"/></svg></span></li>
      <li>jbergeron@kalvento.com <span class="icon"><svg width="10" height="10"><use href="#i-mail"/></svg></span></li>
      <li>kalvento.com <span class="icon"><svg width="10" height="10"><use href="#i-web"/></svg></span></li>
    </ul>
    <div class="holder">
      <p class="holder__name">Julie Bergeron <small>MBA</small></p>
      <p class="holder__role">Vice President | Operations</p>
      <p class="holder__address">410-218 Belanger East,<br>Laval (Quebec) Canada H7A 2K9</p>
    </div>
    <span class="accent-line"></span>
  </section>

  <section class="card card--front">
    <div class="brand-name">kalvento</div>
    <ul class="contacts">
      <li>+1.555.210.0455 <span class="icon"><svg width="10" height="10"><use href="#i-phone"/></svg></span></li>
      <li>otremblay@kalvento.com <span class="icon"><svg width="10" height="10"><use href="#i-mail"/></svg></span></li>
      <li>kalvento.com <span class="icon"><svg width="10" height="10"><use href="#i-web"/></svg></span></li>
    </ul>
    <div class="holder">
      <p class="holder__name">Olivier Tremblay <small>P.Eng.</small></p>
      <p class="holder__role">Director | Engineering</p>
      <p class="holder__address">410-218 Belanger East,<br>Laval (Quebec) Canada H7A 2K9</p>
    </div>
    <span class="accent-line"></span>
  </section>
</main>
</body>
</html>
```